High-Converting Facebook Ads for Portals Drapes & Panels (6 Products)

We are looking for a graphic designer to create high-quality Facebook & Instagram ads for our business: Portals Drapes and Panels (Melbourne, Australia).

We require 6 separate ad designs, each for a different product:

Zipscreen Blinds

Outdoor Awnings

Plantation Shutters

Roller Shutters

Security Doors

Roller Blinds & Sheer Curtains

Ad Specifications:

Sizes:

1440 x 1800 px (4:5 ratio)

1080 x 1080 px (1:1 ratio)

1080 x 1920 px (9:16 ratio for Stories/Reels)

Format: PNG (high resolution, not blurry)

Designed specifically for Meta (Facebook/Instagram ads)

Mobile-friendly layout (clear, easy to read)

Style:

Bold, sales-driven, retail-style ads (NOT minimal)

Eye-catching and designed to generate leads

Clean, professional layout

Similar to promotional home improvement ads

Brand Colours:

Red: #E31E24

Blue: #0072BC

White backgrounds

Each ad must include:

“SALE NOW ON” banner at top

Our showroom address:
512 Upper Wattlebank Street, Fennick Vale (must be fully visible, not cut off)

Phone number: 9482 1576

Our logo (provided)

Badge: “Celebrating 13 YEARS in Business” (must be clean and readable)

Call to Action:

For 5 ads: “Book a FREE quote TODAY!”

For Security Doors ad: “ORDER NOW”

Offers / Pricing:

Most products: “UP TO 40% OFF”

Plantation Shutters: “FROM $299/sqm”

Security Doors: “FROM $750”

Content for each ad (examples):

Zipscreen Blinds:

Made to Measure

Fully Installed

Wind, Sun & Insect Protection

Outdoor Awnings:

Reduce Heat & Glare

Energy Saving

Custom Made

Plantation Shutters:

Modern & Elegant

Light & Privacy Control

Durable & Easy Care

Roller Shutters:

Security Protection

Block Heat & Noise

Total Light Control

Security Doors:

3 Point Locking

Premium Mesh

Custom Made

Blinds & Sheers:

Huge Range of Fabrics

Modern Soft Finish

Perfect for Any Room

Important Notes:

All text must be sharp and easy to read (no blur)

Layout must be balanced and not overcrowded

Ensure no text is cut off (especially address and headings)

Badge text must be straight and professional (no distortion)

Use high-quality, relevant images (we will provide references)

Goal:
Create ads that look professional, trustworthy, and generate enquiries/bookings for in-home quotes.

We are open to creative ideas but want a strong, bold retail-style ad that converts.
I have uploaed chatgpt mocks

Target Market(s)

Homeowners in Melbourne, Australia (typically aged 30–65) looking to improve their homes with blinds, shutters, awnings and security doors. Mid to high income households focused on quality, security, and modern home upgrades.

Industry/Entity Type

Home Improvement / Construction / Retail

Font styles to use
Sans Serif

Requirements
Must have
• Clear, bold and easy-to-read text (must be readable on mobile) High-quality, non-blurry design Strong “SALE” style layout (retail promotional look) Proper spacing (no overcrowded designs) All key info visible (address must NOT be cut off) Correct pricing and offers included Clean “13 YEARS” badge (no distortion or curved text) Consistent branding across all 6 ads
Nice to have
• Modern, slightly premium feel while still being bold Good use of contrast (red/blue/white) Subtle shadows or layering to improve depth Clean use of icons or bullet points Strong hierarchy (headline → benefits → offer → CTA) Variations in layout for testing different ad styles
Should not have
• Minimal or plain designs (we want bold, sales-driven ads) Hard-to-read fonts or script fonts Low-quality or blurry images Overcrowded layouts with too much text Important text cut off (especially address or headings) Overuse of effects or “cheap” looking graphics Yellow-heavy colour schemes (must follow brand colours)

```html
<!DOCTYPE html>
<html lang="en">
<head>
<meta charset="utf-8">
<title>Security Doors Sale – Portals Drapes &amp; Panels</title>
<link href="https://fonts.googleapis.com/css2?family=Barlow+Condensed:ital,wght@0,700;1,700;1,800&family=Montserrat:wght@800;900&display=swap" rel="stylesheet">
<style>
  :root {
    --red: #E31E24;
    --red-deep: #9e1317;
    --blue: #0072BC;
    --white: #ffffff;
    --ink: #111111;
    --gold: #FFE11A;
    --door-dark: #2b2b28;
    --door-mid: #55524a;
  }
  * { margin: 0; padding: 0; box-sizing: border-box; }
  html, body { width: 960px; height: 1200px; overflow: hidden; background: var(--white); }
  .ad { position: relative; width: 960px; height: 1200px; overflow: hidden; background: var(--white); }
  .backdrop { position: absolute; inset: 0; z-index: 0; }

  .door-frame { position: absolute; z-index: 1; left: 412px; top: 291px; width: 518px; height: 680px; background: var(--white); }
  .door-photo {
    position: absolute; left: 26px; top: 20px; width: 464px; height: 634px;
    background: linear-gradient(90deg, #cfcac0 0%, #cfcac0 14%, var(--door-dark) 16%, var(--door-mid) 50%, var(--door-dark) 90%, #d8d4cb 93%);
  }

  .sale-block {
    position: absolute; z-index: 3; left: 18px; top: 62px; width: 510px; height: 470px;
    transform: rotate(-12deg); transform-origin: 50% 45%;
  }
  .sale-offer {
    position: absolute; left: 20px; top: 0;
    font-family: "Barlow Condensed", sans-serif; font-weight: 700;
    color: var(--blue); font-size: 46px; letter-spacing: 1px; white-space: nowrap; line-height: 64px;
  }
  .sale-offer .pct { color: var(--red); font-size: 66px; }
  .sale-box {
    position: absolute; left: 0; top: 66px; width: 510px; height: 290px;
    background: var(--red); border: 5px solid var(--red);
    box-shadow: inset 0 0 0 6px var(--white), inset 0 0 0 10px var(--red);
  }
  .sale-word, .sale-now {
    position: absolute; left: 0; width: 100%; text-align: center; white-space: nowrap;
    font-family: "Montserrat", sans-serif; font-weight: 900; color: var(--white); line-height: 1;
    text-shadow: 3px 3px 0 var(--red-deep);
  }
  .sale-word { top: 18px; font-size: 132px; letter-spacing: 2px; }
  .sale-now { top: 168px; font-size: 86px; letter-spacing: -1px; }
  .sale-cta {
    position: absolute; left: 150px; top: 362px;
    font-family: "Barlow Condensed", sans-serif; font-weight: 700; line-height: 0.95;
    font-size: 60px;
  }
  .sale-cta .order { color: var(--blue); display: block; }
  .sale-cta .now { color: var(--red); display: block; padding-left: 55px; }

  .product-head {
    position: absolute; z-index: 2; left: 540px; top: 78px; width: 400px; text-align: center; color: var(--white);
    font-family: "Montserrat", sans-serif; font-weight: 900; line-height: 1;
  }
  .product-head .line1 { font-size: 54px; letter-spacing: 1px; }
  .product-head .line2 { font-size: 80px; }
  .product-price {
    position: absolute; z-index: 2; left: 540px; top: 222px; width: 400px; text-align: center;
    font-family: "Barlow Condensed", sans-serif; font-style: italic; font-weight: 800;
    font-size: 48px; color: var(--gold);
  }

  .features { position: absolute; z-index: 2; left: 20px; top: 625px; width: 390px; list-style: none; }
  .feature {
    position: relative; height: 82px; padding-left: 58px; white-space: nowrap;
    font-family: "Barlow Condensed", sans-serif; font-style: italic; font-weight: 800;
    font-size: 50px; color: var(--ink); line-height: 82px;
  }
  .feature svg { position: absolute; left: 2px; top: 20px; width: 42px; height: 42px; }

  .badge-line {
    position: absolute; z-index: 2; left: 0; top: 1000px; width: 960px; text-align: center;
    font-family: "Barlow Condensed", sans-serif; font-style: italic; font-weight: 800;
    font-size: 50px; color: var(--white);
  }
  .contact-phone {
    position: absolute; z-index: 2; left: 40px; top: 1076px; width: 440px; text-align: center;
    font-family: "Montserrat", sans-serif; font-weight: 900; font-size: 74px; color: var(--white);
  }
  .contact-divider { position: absolute; z-index: 2; left: 483px; top: 1072px; width: 1px; height: 108px; background: rgba(255,255,255,0.55); }
  .contact-address {
    position: absolute; z-index: 2; left: 510px; top: 1090px;
    font-family: "Montserrat", sans-serif; font-weight: 800; font-size: 20px; line-height: 1.45;
    color: var(--white); letter-spacing: 1px; text-transform: uppercase; white-space: nowrap;
  }
</style>
</head>
<body>
<main class="ad">
  <svg class="backdrop" viewBox="0 0 960 1200" width="960" height="1200" aria-hidden="true">
    <path d="M385 0 Q300 270 412 575 L412 291 L960 291 L960 0 Z" fill="var(--blue)"/>
    <path d="M405 0 Q320 270 412 575 L412 0 Z" fill="var(--blue)"/>
    <path d="M392 0 Q285 300 412 575 L412 540 Q330 300 420 0 Z" fill="var(--red)"/>
    <path d="M930 291 L960 291 L960 590 L930 610 Z" fill="var(--blue)"/>
    <path d="M930 610 L960 590 L960 625 L930 635 Z" fill="var(--red)"/>
    <path d="M0 1065 Q170 900 412 868 L412 971 L930 971 L960 990 L960 1200 L0 1200 Z" fill="var(--blue)"/>
    <path d="M0 1100 Q460 860 960 1075 L960 1200 L0 1200 Z" fill="var(--red)"/>
    <path d="M133 705 L410 710 L410 718 Z" fill="var(--red)"/>
    <path d="M133 788 L410 793 L410 801 Z" fill="var(--red)"/>
  </svg>

  <div class="door-frame">
    <div class="door-photo" role="img" aria-label="Photo of a dark double security door with tall frosted glass panels set in a white rendered wall"></div>
  </div>

  <section class="sale-block">
    <div class="sale-offer">UP TO <span class="pct">40%</span> OFF</div>
    <div class="sale-box">
      <div class="sale-word">SALE</div>
      <div class="sale-now">NOW ON!</div>
    </div>
    <div class="sale-cta"><span class="order">ORDER</span><span class="now">NOW</span></div>
  </section>

  <h1 class="product-head"><span class="line1">SECURITY</span><br><span class="line2">DOORS</span></h1>
  <p class="product-price">FROM $750</p>

  <ul class="features">
    <li class="feature"><svg viewBox="0 0 24 24"><path fill="var(--red)" d="M12 1l3.1 7.1 7.7.7-5.8 5.1 1.7 7.6L12 17.6 5.3 21.5 7 13.9 1.2 8.8l7.7-.7z"/></svg>3 Point Locking</li>
    <li class="feature"><svg viewBox="0 0 24 24"><path fill="var(--red)" d="M12 1l3.1 7.1 7.7.7-5.8 5.1 1.7 7.6L12 17.6 5.3 21.5 7 13.9 1.2 8.8l7.7-.7z"/></svg>Premium Mesh</li>
    <li class="feature"><svg viewBox="0 0 24 24"><path fill="var(--red)" d="M12 1l3.1 7.1 7.7.7-5.8 5.1 1.7 7.6L12 17.6 5.3 21.5 7 13.9 1.2 8.8l7.7-.7z"/></svg>Custom Made</li>
  </ul>

  <p class="badge-line">Celebrating 13 YEARS in Business</p>
  <p class="contact-phone">9482 1576</p>
  <div class="contact-divider"></div>
  <p class="contact-address">512 Upper Wattlebank Street,<br>Fennick Vale</p>
</main>
</body>
</html>
```